Custom beer tap decals, Halvett Brewery, Tasmania, Australia.

UPDATE 22/6/2017

Based on designs received so far, Im after more of a bold/clean design. This must standout. See attached example.

Beer tap decals for 4 different products. Rustic/English feel, with some modern vibrancy, maintain original branding as much as possible.
The size bust be a 95mm circle. Please see attached artwork.
The same branding theme must carry across all four designs. While each can be different, the core branding remaining the same is important.
Happy for different fonts to be used, but they must be clearly readable. The font for the 'Halvett Brewery' component must remain the same.
The colours used in the flag banner part of the decal must remain the same as these reflect the colours on our bottle labels.

Highlighting the 'Made in Tasmania' component would be nice, although not entirely necessary.

Plus a 'Limited Release; design including white space where one off beers can be written in permanent marker, we brew quite a few small batch beers per year and it doesn’t make sense to have custom decals for each. Having a generic limited release decal that we can change ourselves would be a big help.

Target Market(s)

Graphic design, beer, brewery.

Industry/Entity Type

Brewery

Colors

Designer to choose colors to be used in the design.

Requirements
Must have
• 'Halvett Brewery' component of supplied decals must remain. Would be nice to incorporate some of the shield elements, but isn't vital.
Nice to have
• Rustic/earth themes, with a modern twist and vibrance.

```html
<!DOCTYPE html>
<html lang="en">
<head>
<meta charset="utf-8">
<title>Halvett Brewery – Tap Decals</title>
<link rel="stylesheet" href="https://fonts.googleapis.com/css2?family=Cinzel+Decorative:wght@700&family=Cinzel:wght@600&family=Playfair+Display:wght@600&family=Pinyon+Script&display=swap">
<style>
  :root {
    --canvas: #ffffff;
    --ring-black: #0d0d0d;
    --ring-green: #1f7a3a;
    --field-green: #12914a;
    --field-green-dark: #0b6b34;
    --ink: #111111;
    --label-white: #ffffff;
    --bitter: #c8963f;
    --stout: #efeec2;
    --red-ale: #a9353b;
    --pale-ale: #f08a2a;
    --hop-light: #8cc43c;
    --hop-dark: #2f6b2e;
  }
  html, body {
    margin: 0;
    padding: 0;
    width: 1200px;
    height: 1172px;
    overflow: hidden;
    background: var(--canvas);
  }
  .sheet {
    position: relative;
    width: 1200px;
    height: 1172px;
  }
  .defs { position: absolute; width: 0; height: 0; }
  .decal {
    position: absolute;
    width: 476px;
    height: 476px;
  }
  .decal--bitter { left: 68px;  top: 74px;  color: var(--bitter); }
  .decal--stout  { left: 608px; top: 74px;  color: var(--stout); }
  .decal--red    { left: 68px;  top: 622px; color: var(--red-ale); }
  .decal--pale   { left: 608px; top: 622px; color: var(--pale-ale); }
  .origin-line {
    font-family: "Cinzel", serif;
    font-size: 22px;
    letter-spacing: 2px;
    fill: var(--label-white);
  }
  .brand-name {
    font-family: "Cinzel Decorative", serif;
    font-size: 82px;
    font-weight: 700;
    fill: var(--label-white);
  }
  .brand-sub {
    font-family: "Cinzel", serif;
    font-size: 28px;
    font-weight: 600;
    fill: var(--label-white);
  }
  .batch {
    font-family: "Pinyon Script", cursive;
    font-size: 38px;
    fill: var(--ink);
  }
  .beer-name {
    font-family: "Playfair Display", serif;
    font-weight: 600;
    font-size: 104px;
    fill: var(--ink);
  }
</style>
</head>
<body>
<main class="sheet">

  <svg class="defs" aria-hidden="true">
    <defs>
      <clipPath id="field-clip"><circle r="272"/></clipPath>
      <pattern id="field-stripes" width="40" height="600" patternUnits="userSpaceOnUse">
        <rect width="20" height="600" fill="#ffffff" opacity="0.06"/>
      </pattern>
      <radialGradient id="field-shade" r="0.6">
        <stop offset="0.6" stop-color="#000" stop-opacity="0"/>
        <stop offset="1" stop-color="#000" stop-opacity="0.35"/>
      </radialGradient>
      <linearGradient id="hop-tone" x1="0" y1="0" x2="1" y2="1">
        <stop offset="0" stop-color="var(--hop-dark)"/>
        <stop offset="0.5" stop-color="var(--hop-light)"/>
        <stop offset="1" stop-color="var(--hop-dark)"/>
      </linearGradient>
      <path id="origin-arc" d="M -200 0 A 200 200 0 0 1 200 0" transform="translate(0 -15)"/>
      <path id="brand-arc" d="M -215 -85 Q 0 -160 215 -85"/>

      <symbol id="decal-base" viewBox="-300 -300 600 600">
        <circle r="298" fill="var(--ring-black)"/>
        <circle r="283" fill="var(--ring-green)"/>
        <circle r="277" fill="var(--ring-black)"/>
        <g clip-path="url(#field-clip)">
          <rect x="-300" y="-300" width="600" height="600" fill="var(--field-green)"/>
          <path class="flag-band" d="M -190 200 Q -40 -45 300 -55 L 300 300 L -300 300 Z" fill="currentColor"/>
          <rect x="-300" y="-300" width="600" height="600" fill="url(#field-stripes)"/>
          <rect x="-300" y="225" width="600" height="80" fill="#000" opacity="0.15"/>
          <rect class="batch-band" x="-300" y="173" width="600" height="52" fill="var(--label-white)"/>
          <rect x="-300" y="-300" width="600" height="600" fill="url(#field-shade)"/>
          <g role="img" aria-label="Illustration of hop cones with leaves">
            <path d="M -262 -60 Q -180 -75 -120 -40 Q -40 -20 0 60 Q 30 110 -20 150 Q -60 200 -150 185 Q -230 175 -262 110 Z" fill="url(#hop-tone)"/>
          </g>
        </g>
        <text class="origin-line" text-anchor="middle"><textPath href="#origin-arc" startOffset="50%">- MADE IN TASMANIA -</textPath></text>
        <text class="brand-name" text-anchor="middle"><textPath href="#brand-arc" startOffset="50%">HALVETT</textPath></text>
        <text class="brand-sub" x="0" y="-80" text-anchor="middle">BREWERY</text>
        <text class="batch" x="-10" y="212" text-anchor="middle">Batch No.5</text>
      </symbol>
    </defs>
  </svg>

  <svg class="decal decal--bitter" viewBox="-300 -300 600 600" role="img" aria-label="English Bitter tap decal">
    <use href="#decal-base" x="-300" y="-300" width="600" height="600"/>
    <g transform="scale(.72 1)">
      <text class="beer-name" x="308" y="45" text-anchor="end">English</text>
      <text class="beer-name" x="300" y="130" text-anchor="end">Bitter</text>
    </g>
  </svg>

  <svg class="decal decal--stout" viewBox="-300 -300 600 600" role="img" aria-label="Irish Stout tap decal">
    <use href="#decal-base" x="-300" y="-300" width="600" height="600"/>
    <g transform="scale(.72 1)">
      <text class="beer-name" x="305" y="45" text-anchor="end">Irish</text>
      <text class="beer-name" x="300" y="130" text-anchor="end">Stout</text>
    </g>
  </svg>

  <svg class="decal decal--red" viewBox="-300 -300 600 600" role="img" aria-label="Irish Red Ale tap decal">
    <use href="#decal-base" x="-300" y="-300" width="600" height="600"/>
    <g transform="scale(.72 1)">
      <text class="beer-name" x="335" y="45" text-anchor="end">Irish Red</text>
      <text class="beer-name" x="210" y="130" text-anchor="end">Ale</text>
    </g>
  </svg>

  <svg class="decal decal--pale" viewBox="-300 -300 600 600" role="img" aria-label="Pale Ale tap decal">
    <use href="#decal-base" x="-300" y="-300" width="600" height="600"/>
    <g transform="scale(.72 1)">
      <text class="beer-name" x="280" y="45" text-anchor="end">Pale</text>
      <text class="beer-name" x="210" y="130" text-anchor="end">Ale</text>
    </g>
  </svg>

</main>
</body>
</html>
```